Email Signature

We would like to have an email Signature designed.
We have an idea, and a logo that we would like to be make more professional in design and look.

```html
<!DOCTYPE html>
<html lang="en">
<head>
<meta charset="utf-8">
<title>Harbor Line Consulting — Letterhead</title>
<link rel="stylesheet" href="https://fonts.googleapis.com/css2?family=Mulish:wght@400;700;800&family=Arimo:wght@700&family=Carlito:wght@700&display=swap">
<style>
  :root {
    --canvas: #d9d9d9;
    --paper: #ffffff;
    --brand-blue: #0c6db6;
    --brand-orange: #e84e1f;
    --text-blue: #1170b8;
    --white: #ffffff;
  }
  * { box-sizing: border-box; margin: 0; padding: 0; }
  html, body {
    width: 1200px; height: 1200px; overflow: hidden;
    background: var(--canvas);
  }
  .letterhead {
    position: absolute;
    left: 205px; top: 30px;
    width: 789px; height: 1140px;
    background: var(--paper);
    box-shadow: 0 4px 18px rgba(0,0,0,0.18);
  }
  .brand {
    position: absolute;
    left: 294px; top: 25px;
    width: 200px; height: 84px;
    display: flex; flex-direction: column; align-items: center; justify-content: center;
    gap: 4px;
    font-family: "Mulish", sans-serif;
    font-weight: 800;
    color: var(--brand-blue);
  }
  .brand-name { display: flex; align-items: center; gap: 7px; font-size: 17px; line-height: 1.1; text-align: center; }
  .brand-dot { width: 14px; height: 14px; border-radius: 50%; background: var(--brand-orange); flex: none; }
  .brand-web { font-size: 11px; }
  .subject {
    position: absolute; left: 70px; top: 268px;
    font-family: "Arimo", sans-serif; font-weight: 700;
    font-size: 20.5px; color: var(--text-blue);
  }
  .body-copy {
    position: absolute; left: 70px; top: 320px; width: 660px;
    font-family: "Mulish", sans-serif; font-size: 17px; line-height: 24.6px;
    color: var(--text-blue);
  }
  .body-copy strong { font-weight: 800; }
  .signature {
    position: absolute; left: 70px; top: 952px;
    font-family: "Carlito", sans-serif; font-weight: 700;
    font-size: 27px; color: var(--text-blue);
  }
  .footer-band {
    position: absolute; left: 0; bottom: 0; width: 789px; height: 43px;
  }
  .footer-band svg { position: absolute; inset: 0; }
  .footer-contact {
    position: absolute; left: 18px; top: 0; height: 43px;
    display: flex; align-items: center; gap: 8px;
    font-family: "Mulish", sans-serif; color: var(--white); font-size: 13px;
  }
  .footer-contact .name { font-weight: 800; font-size: 15px; }
  .footer-contact .divider { font-weight: 800; }
  .footer-phone {
    position: absolute; right: 19px; top: 0; height: 43px;
    display: flex; align-items: center;
    font-family: "Mulish", sans-serif; font-weight: 800; font-size: 12.5px; color: var(--white);
  }
</style>
</head>
<body>
  <main class="letterhead">
    <div class="brand">
      <div class="brand-name"><span class="brand-dot"></span>Harbor Line Consulting</div>
      <div class="brand-web">www.harborline.com.au</div>
    </div>

    <h1 class="subject">Subject Line: Loreum Ipsum Dolor Sit Amet.</h1>

    <div class="body-copy">
      <p><strong>Lorem ipsum</strong> dolor sit amet, consectetur adipiscing elit. Proin fringilla ac turpis ac consectetur. Donec quis turpis ac eros auctor pharetra. Praesent rutrum felis lectus, eget pulvinar enim rutrum a. Quisque volutpat dui vel elit rutrum eleifend. Sed suscipit velit at nunc facilisis, sit amet euismod velit tempus. Duis facilisis lectus ut ornare luctus.</p>
      <p>Vestibulum ante ipsum primis in faucibus orci luctus et ultrices posuere cubilia Curae</p>
      <p>Nulla consectetur lacinia sem. Proin vehicula id mi eget vulputate. Nunc lacinia tellus a malesuada tincidunt. Proin iaculis interdum sem hendrerit tempus.</p>
      <p>Curabitur tincidunt nec magna sed porttitor. Fusce hendrerit varius urna eget mollis. Nulla imperdiet sollicitudin lacus.</p>
      <p>Nunc ornare ullamcorper quam, id lacinia mi scelerisque nec. Aliquam efficitur tellus mauris, ut lobortis massa iaculis quis. Curabitur purus ante, dapibus vitae gravida nec, lobortis sed ex. Aenean sollicitudin orci erat, sed rhoncus lacus consectetur nec. Nulla viverra dolor finibus nisi lacinia finibus. Vestibulum ac sapien velit. Phasellus in facilisis erat.</p>
      <p>Fusce sagittis nisi nulla, a consequat lacus imperdiet eu. In eget tellus porta, vulputate dui id, fringilla lectus.</p>
      <p>&nbsp;Cras blandit posuere orci at mattis. Pellentesque ac felis metus. Nullam mattis non mauris quis laoreet. Ut tortor lorem, iaculis eu porta ac, congue ac lorem. Quisque finibus id dolor fermentum aliquam.</p>
      <p>&nbsp;Vestibulum pulvinar, lorem nec ornare ultricies, augue metus posuere purus, sed tristique dui lectus non nulla.</p>
    </div>

    <div class="signature">Signature</div>

    <footer class="footer-band">
      <svg width="789" height="43" viewBox="0 0 789 43" aria-hidden="true">
        <rect x="0" y="0" width="789" height="43" fill="var(--brand-blue)"/>
        <polygon points="0,0 418,0 375,43 0,43" fill="var(--brand-orange)"/>
        <polygon points="418,0 426,0 383,43 375,43" fill="var(--white)"/>
      </svg>
      <div class="footer-contact">
        <span class="name">Sam Porter</span>
        <span class="divider">|</span>
        <span class="role">Client Relations</span>
      </div>
      <div class="footer-phone">M +61491570156</div>
    </footer>
  </main>
</body>
</html>
```